Professional and creatice Life Coach - Business Card design

I just relaunched my website and now i a need a correspoonding business card for my task as life coach. My website is www.dlorvan.net as reference. The compass is kind of a symbol for my work, as I help people navigate through their challenging phases in life. The business card should be colorful, but not too playful as I also adress business people. So it sould be creative, but professional (also to suport my other business as Management Consultant)

Target Market(s)

People who want to get teir problems resolved, in business, partnership and other personal realms

Industry/Entity Type

Life Coaching

Contact Information for Business Card

Front side should include Name, Phone number, Email, Website and address

Font styles to use
Sans Serif

Colors
add136

Requirements
Must have
• "Mag. Benedikt Haufmoll" -> Name
"Energetische Praxis" -> Jobtitle (describing my profession as life coach)
colours and style should match my website www.dlorvan.net
Nice to have
• a compass as a symbol

```html
<!DOCTYPE html>
<html lang="de">
<head>
<meta charset="utf-8">
<title>Visitenkarte – Benedikt Haufmoll</title>
<link rel="stylesheet" href="https://fonts.googleapis.com/css2?family=Lato:wght@300;400;700&display=swap">
<style>
  :root {
    --backdrop: #bcbdc0;
    --card-light: #ffffff;
    --card-dark: #000000;
    --ink: #111111;
    --lime: #add136;
    --lime-soft: #e4efc6;
    --divider: #b8b8b8;
  }
  * { box-sizing: border-box; margin: 0; padding: 0; }
  html, body {
    width: 1022px; height: 1200px; overflow: hidden;
    background: var(--backdrop);
    font-family: "Lato", sans-serif;
    color: var(--ink);
  }
  .sheet { position: relative; width: 1022px; height: 1200px; }
  .card {
    position: absolute; left: 23px; width: 976px; height: 558px;
  }
  .card--front { top: 23px; background: var(--card-light); }
  .card--back { top: 620px; background: var(--card-dark); }

  .brand {
    position: absolute; left: 0; width: 100%;
    display: flex; flex-direction: column; align-items: center; gap: 14px;
  }
  .card--front .brand { top: 78px; }
  .card--back .brand { top: 220px; }
  .brand__dot {
    width: 64px; height: 64px; border-radius: 50%;
    background: var(--lime-soft);
  }
  .card--back .brand__dot { background: var(--lime); }
  .brand__name {
    font-weight: 700; font-size: 24px; letter-spacing: 4px;
    color: #8a9a7a;
  }
  .card--back .brand__name { color: var(--lime); }

  .identity {
    position: absolute; right: 514px; top: 306px; text-align: right;
  }
  .identity__name { font-size: 35px; font-weight: 400; line-height: 1.1; white-space: nowrap; }
  .identity__name strong { font-weight: 700; }
  .identity__title {
    font-size: 26px; font-weight: 700; color: var(--lime); line-height: 1.2;
  }
  .divider {
    position: absolute; left: 487px; top: 300px; width: 3px; height: 89px;
    background: var(--divider);
  }
  .contacts {
    position: absolute; left: 512px; top: 300px; list-style: none;
  }
  .contacts li {
    display: flex; align-items: center; gap: 14px;
    height: 31.5px; font-size: 28px; font-weight: 300;
  }
  .contacts svg { width: 28px; height: 28px; flex: none; }
  .address {
    position: absolute; left: 0; width: 100%; top: 486px;
    text-align: center; font-size: 28px; font-weight: 400;
  }
</style>
</head>
<body>
<div class="sheet">
  <section class="card card--front">
    <div class="brand">
      <span class="brand__dot"></span>
      <span class="brand__name">HAUFMOLL</span>
    </div>

    <div class="identity">
      <p class="identity__name">Mag. <strong>Benedikt Haufmoll</strong></p>
      <p class="identity__title">ENERGETISCHE PRAXIS</p>
    </div>
    <span class="divider"></span>
    <ul class="contacts">
      <li>
        <svg viewBox="0 0 28 28" aria-hidden="true"><circle cx="14" cy="14" r="14" fill="var(--lime)"/><path d="M10 8c1 0 2 2 2 3s-1 1-1 2 3 4 4 4 1-1 2-1 3 1 3 2-1 2-3 2c-4 0-9-5-9-9 0-2 1-3 2-3z" fill="none" stroke="#fff" stroke-width="1.3"/></svg>
        <span>+43 660 4817392</span>
      </li>
      <li>
        <svg viewBox="0 0 28 28" aria-hidden="true"><circle cx="14" cy="14" r="14" fill="var(--lime)"/><rect x="7" y="9" width="14" height="10" fill="none" stroke="#fff" stroke-width="1.3"/><path d="M7 9l7 6 7-6M7 19l5-5M21 19l-5-5" fill="none" stroke="#fff" stroke-width="1.3"/></svg>
        <span>benedikt@dlorvan.net</span>
      </li>
      <li>
        <svg viewBox="0 0 28 28" aria-hidden="true"><circle cx="14" cy="14" r="14" fill="var(--lime)"/><g fill="none" stroke="#fff" stroke-width="1.2"><circle cx="14" cy="14" r="7"/><ellipse cx="14" cy="14" rx="3" ry="7"/><path d="M7 14h14M8 10.5h12M8 17.5h12"/></g></svg>
        <span>www.dlorvan.net</span>
      </li>
    </ul>
    <p class="address">Lindenrainweg 14, 5412 Obertal, Österreich</p>
  </section>

  <section class="card card--back">
    <div class="brand">
      <span class="brand__dot"></span>
      <span class="brand__name">HAUFMOLL</span>
    </div>
  </section>
</div>
</body>
</html>
```